practice letterhead

I need a letterhead design for a new company that is a veterinary specialty company. I am conservative. I want it to look professional - not "cutesy"

I need my name, credentials, address, phone number and website/email on it.

My personal information is as follows: Marisol Tedder, DVM, DACVIM (Neurology) Certified Veterinary Pain Practitioner (or CVPP) Certified Canine Rehabilitation Therapist (or CCRT) 4170 Larkfield Hwy Dunmore, MA 01744 508-347-6620 marisol.tedder@petspineandcare.com www.petspineandcare.com

```html
<!DOCTYPE html>
<html lang="en">
<head>
<meta charset="utf-8">
<title>Pet Spine and Care Specialty Center – Letterhead</title>
<link rel="stylesheet" href="https://fonts.googleapis.com/css2?family=Roboto+Condensed:wght@500&family=Open+Sans:wght@400;600;700&display=swap">
<style>
  :root {
    --backdrop: #ececec;
    --paper: #f9f9f9;
    --slate: #354a52;
    --sage: #6f9486;
    --ink: #3a3f42;
    --white: #ffffff;
  }
  * { margin: 0; padding: 0; box-sizing: border-box; }
  html, body {
    width: 1200px; height: 800px; overflow: hidden;
    background: var(--backdrop);
    font-family: "Open Sans", Arial, sans-serif;
  }
  .canvas { position: relative; width: 1200px; height: 800px; }

  .sheet {
    position: absolute; top: 112px; width: 407px; height: 573px;
    background: var(--paper);
    border-top: 4px solid var(--slate);
  }
  .sheet--letter { left: 165px; }
  .sheet--cover { left: 614px; }

  .footer-band {
    position: absolute; left: 0; right: 0; bottom: 0; height: 18px;
    background: var(--slate); color: var(--white);
    font-size: 7px; text-align: center; line-height: 18px; letter-spacing: .1px;
  }
  .footer-band strong { font-weight: 700; }

  .brand { position: absolute; display: flex; align-items: center; }
  .brand__dot { border-radius: 50%; background: var(--slate); flex: none; }
  .brand__name {
    font-family: "Roboto Condensed", "Arial Narrow", sans-serif;
    font-weight: 500; color: var(--sage); line-height: 1.02;
  }

  .brand--small { left: 18px; top: 22px; gap: 8px; }
  .brand--small .brand__dot { width: 30px; height: 30px; }
  .brand--small .brand__name { font-size: 11px; }

  .brand--large { left: 30px; top: 242px; gap: 18px; }
  .brand--large .brand__dot { width: 76px; height: 76px; }
  .brand--large .brand__name { font-size: 24px; }

  .contact {
    position: absolute; left: 258px; top: 16px;
    border-left: 1px solid var(--slate); padding-left: 9px;
    font-size: 5.2px; line-height: 1.45; color: var(--sage);
  }
  .contact__name { color: var(--ink); }
  .contact__name strong { font-weight: 700; }
  .contact__phone, .contact__email { color: var(--ink); font-weight: 700; }
  .contact__email span { color: var(--sage); font-weight: 400; }
  .contact abbr { text-decoration: none; color: var(--ink); font-weight: 700; }

  .address {
    position: absolute; left: 0; right: 0; bottom: 24px;
    text-align: center; font-size: 7px; font-weight: 600;
    color: var(--sage); letter-spacing: .2px; text-transform: uppercase;
  }
</style>
</head>
<body>
<main class="canvas">
  <section class="sheet sheet--letter" aria-label="Letterhead">
    <div class="brand brand--small">
      <span class="brand__dot"></span>
      <span class="brand__name">Pet Spine and Care<br>Specialty Center</span>
    </div>
    <div class="contact">
      <p class="contact__name"><strong>Marisol Tedder</strong>, DVM, DACVIM (Neurology)</p>
      <p>Certified Veterinary Pain Practitioner (<abbr>CVPP</abbr>)</p>
      <p>Certified Canine Rehabilitation Therapist (<abbr>CCRT</abbr>)</p>
      <p class="contact__phone">508-347-6620</p>
      <p class="contact__email">marisol.tedder<span>@petspineandcare.com</span></p>
    </div>
    <p class="address">4170 Larkfield Hwy Dunmore, MA 01744</p>
    <div class="footer-band">www.<strong>petspineandcare</strong>.com</div>
  </section>

  <section class="sheet sheet--cover" aria-label="Letterhead cover">
    <div class="brand brand--large">
      <span class="brand__dot"></span>
      <span class="brand__name">Pet Spine and Care<br>Specialty Center</span>
    </div>
    <div class="footer-band">www.<strong>petspineandcare</strong>.com</div>
  </section>
</main>
</body>
</html>
```